New business needs it's first website designed and coded for Wordpress

This is a new website for a new business. The business is called The Remote Tech Specialist (TRTS). The business is based across multiple countries with the goal of providing workers in the Philippines opportunities to find work in international companies based in Australia, Singapore and New Zealand. The target market for TRTS is large enterprises (initially in Australia) looking for well legally structured business that knows how to recruit the top IT professionals and ensure that they are happy, all compliance, taxes and legals and professionally done and all services contracts are local to ensure enforceability.

We are looking for 10 pages (6 templates) for the website as follows:
Home
About Us
Services
Work from home full-timers
Work from office full-times
Work from home contractors
Work from office contractors
Careers Job Search
Employers Contact Us
Candidates Register your interest

Target Market(s)

IT Professionals in the Philippines & large enterprises in Australia, Singapore and New Zealand

Industry/Entity Type

IT Recruitment

Coding

Coded - Design and coding required

Number of Pages Required

5+ page

Requirements
Must have
• Please based style off logo file attached.

```html
<!DOCTYPE html>
<html lang="en">
<head>
<meta charset="UTF-8">
<title>The Remote Tech Specialist</title>
<link href="https://fonts.googleapis.com/css2?family=Archivo+Black&family=Inter:wght@400;500;600;700;800&display=swap" rel="stylesheet">
<style>
:root{
  --blue:#00a8ec;
  --blue-dark:#0a4d72;
  --navy:#06223a;
  --black:#000;
  --ink:#1a1a1a;
  --grey-bg:#f4f4f4;
  --field:#f7f8f9;
  --field-line:#5fc6f2;
  --white:#fff;
  --head:"Archivo Black", "Arial Black", sans-serif;
  --body:"Inter", Arial, sans-serif;
}
*{margin:0;padding:0;box-sizing:border-box}
html,body{width:1200px;height:3202px;overflow:hidden;background:var(--white);font-family:var(--body);color:var(--ink)}
.page{position:relative;width:1200px;height:3202px}
.abs{position:absolute}
.eyebrow{font-family:var(--body);font-weight:800;font-size:12px;letter-spacing:3px;color:var(--blue);text-transform:uppercase}
.btn{position:absolute;display:flex;align-items:center;justify-content:center;font-family:var(--body);font-weight:800;font-size:11px;letter-spacing:2px;text-transform:uppercase;background:var(--blue);color:var(--white)}
.btn.light{background:var(--white);color:var(--blue)}
.brand{font-family:var(--head);letter-spacing:-1px;line-height:1}

/* nav */
.nav{position:absolute;left:0;top:0;width:1200px;height:66px;background:var(--grey-bg);border-bottom:1px solid #ddd}
.nav .brand{position:absolute;left:75px;top:17px;font-size:30px;color:var(--blue)}
.nav ul{position:absolute;right:74px;top:26px;display:flex;gap:29px;list-style:none;font-size:10.5px;color:#333}
.nav li.active{font-weight:700;color:#000;position:relative}
.nav li.active::after{content:"";position:absolute;left:50%;top:20px;width:12px;height:2px;margin-left:-6px;background:var(--blue)}
.nav .caret{display:inline-block;margin-left:5px;border:4px solid transparent;border-top-color:var(--blue);vertical-align:-1px}

/* hero */
.hero{position:absolute;left:0;top:66px;width:1200px;height:546px;overflow:hidden}
.hero .copy{position:absolute;left:0;width:1200px;text-align:center;color:var(--white)}
.hero .kicker{top:243px;font-weight:800;font-size:12.5px;letter-spacing:3px}
.hero h1.copy{top:268px;font-family:var(--head);font-size:50px;line-height:52px;letter-spacing:-1px;text-transform:uppercase}
.hero p.copy{top:391px;font-size:13.5px;line-height:18px;left:285px;width:630px}

/* about */
.about-photo{left:188px;top:696px;width:402px;height:456px;background:linear-gradient(160deg,#c9d4d8 0%,#5b7285 45%,#2c3d5c 75%,#8a7060 100%)}
.about .eyebrow{left:621px;top:724px}
.about h2{left:621px;top:748px;font-family:var(--head);font-size:37px;line-height:41px;letter-spacing:-1px;text-transform:uppercase;color:#111}
.about p{left:621px;width:392px;font-size:10.5px;line-height:18.2px;color:#333}

/* services */
.services{position:absolute;left:0;top:1240px;width:1200px;height:620px;background:var(--black);overflow:hidden}
.services .center{position:absolute;left:0;width:1200px;text-align:center;color:var(--white)}
.services .center.eyebrow{color:var(--blue)}
.services h2{font-family:var(--head);font-size:36px;line-height:41px;letter-spacing:-1px;text-transform:uppercase}
.services p{font-size:10.5px;line-height:19.5px}
.svc-label{position:absolute;font-family:var(--head);font-size:11px;line-height:14px;color:var(--white);text-transform:uppercase;letter-spacing:-.2px}

/* careers banner */
.careers{position:absolute;left:25px;top:1885px;width:1150px;height:257px;background:var(--blue);clip-path:polygon(0 0,100% 0,100% 197px,1090px 100%,60px 100%,0 197px)}
.careers .brand{position:absolute;left:154px;top:78px;font-size:92px;color:var(--white);letter-spacing:-2px}
.careers .divider{position:absolute;left:505px;top:92px;width:1px;height:73px;background:rgba(255,255,255,.6)}
.careers .eyebrow{position:absolute;left:549px;top:54px;color:#0b2c44}
.careers h2{position:absolute;left:549px;top:78px;font-family:var(--head);font-size:35px;line-height:41px;letter-spacing:-1px;color:var(--white);text-transform:uppercase}

/* contact */
.contact .center{position:absolute;left:0;width:1200px;text-align:center}
.contact h2{font-family:var(--head);font-size:36px;letter-spacing:-1px;text-transform:uppercase;color:#111}
.contact p{font-size:10.5px;line-height:18px;color:#333}
.field{position:absolute;left:328px;width:544px;height:34px;background:var(--field);border:1px solid var(--field-line);font-size:9.5px;color:#444;text-align:center;padding-top:11px}
.field.area{height:151px;padding-top:11px}

/* footer */
.footer{position:absolute;left:0;top:2822px;width:1200px;height:334px;background:var(--black);color:var(--white)}
.footer .brand{position:absolute;left:188px;top:80px;font-size:30px;color:var(--white)}
.footer h4{position:absolute;top:105px;font-family:var(--head);font-size:11px;letter-spacing:-.2px;text-transform:uppercase}
.footer .about-text{position:absolute;left:188px;top:133px;width:270px;font-size:10.5px;line-height:18.2px}
.footer ul{position:absolute;left:518px;top:133px;list-style:none;font-size:10.5px;line-height:18.2px}
.social{position:absolute;top:227px;width:26px;height:26px;border-radius:50%}
.footer .newsletter-field{position:absolute;left:772px;top:130px;width:240px;height:34px;background:var(--white);color:#444;font-size:9.5px;padding:12px 0 0 15px}
.copyright{position:absolute;left:0;top:3156px;width:1200px;height:46px;text-align:center;font-size:10.5px;color:#333;padding-top:14px}
</style>
</head>
<body>
<div class="page">

  <header class="nav">
    <div class="brand">TRTS</div>
    <ul>
      <li class="active">Home</li>
      <li>About Us</li>
      <li>Services<span class="caret"></span></li>
      <li>Careers Job Search</li>
      <li>Employers Contact Us</li>
      <li>Candidates Register your interest</li>
    </ul>
  </header>

  <section class="hero">
    <div class="abs" role="img" aria-label="Photo of two office professionals working with a laptop and tablet" style="left:0;top:0;width:1200px;height:546px;background:linear-gradient(180deg,#b8a48e 0%,#6a5a52 30%,#2d2a2c 60%,#141a22 100%)"></div>
    <svg class="abs" style="left:0;top:0" width="1200" height="546" viewBox="0 0 1200 546">
      <defs>
        <linearGradient id="wedgeL" x1="0" y1="0" x2="0" y2="1"><stop offset="0" stop-color="#14a6e6"/><stop offset="1" stop-color="#0a3d63"/></linearGradient>
        <linearGradient id="fade" x1="0" y1="0" x2="0" y2="1"><stop offset="0" stop-color="#061a2c" stop-opacity="0"/><stop offset="1" stop-color="#061a2c" stop-opacity=".75"/></linearGradient>
      </defs>
      <polygon points="0,0 600,546 0,546" fill="url(#wedgeL)" opacity=".9"/>
      <polygon points="1200,0 600,546 1200,546" fill="url(#wedgeL)" opacity=".9"/>
      <rect x="0" y="200" width="1200" height="346" fill="url(#fade)"/>
    </svg>
    <div class="copy kicker">THE REMOTE TECH SPECIALIST</div>
    <h1 class="copy">Connecting Talent to<br>Opportunity, Seamlessly</h1>
    <p class="copy">Lorem Ipsum is simply dummy text of the printing and typesetting industry. Lorem Ipsum has been the industry's standard dummy text ever since the 1500s,</p>
    <div class="btn" style="left:512px;top:449px;width:176px;height:34px">Search Jobs</div>
  </section>

  <section class="about">
    <div class="abs about-photo" role="img" aria-label="Photo of three young IT professionals reviewing work at a computer"></div>
    <div class="abs eyebrow">About Us</div>
    <h2 class="abs">Your Bridge<br>to Exceptional<br>Talent</h2>
    <p class="abs" style="top:892px">Lorem Ipsum is simply dummy text of the printing and typesetting industry. Lorem Ipsum has been the industry's standard dummy text ever since the 1500s, when an unknown printer took a galley of type and scrambled it to make a type specimen book.</p>
    <p class="abs" style="top:983px">It has survived not only five centuries, but also the leap into electronic typesetting, remaining essentially unchanged. It was popularised in the 1960s with the release of Typeplate sheets containing Lorem Ipsum passages, and more recently with desktop publishing software like Pressline Layout including versions of Lorem Ipsum.</p>
    <div class="btn" style="left:621px;top:1099px;width:176px;height:34px">Read More</div>
  </section>

  <section class="services">
    <svg class="abs" style="left:0;top:0" width="1200" height="620" viewBox="0 0 1200 620">
      <defs>
        <linearGradient id="band" x1="0" y1="0" x2="0" y2="1"><stop offset="0" stop-color="#0b5a82"/><stop offset="1" stop-color="#041522"/></linearGradient>
      </defs>
      <rect x="0" y="432" width="1200" height="188" fill="url(#band)"/>
      <polygon points="0,432 600,620 1200,432" fill="#000"/>
      <g stroke="#00a8ec" stroke-width="1.2" fill="none">
        <line x1="600" y1="287" x2="600" y2="414"/>
        <line x1="539" y1="345" x2="660" y2="345"/>
        <line x1="539" y1="426" x2="660" y2="426"/>
        <circle cx="600" cy="345" r="12" fill="#000"/>
        <circle cx="600" cy="426" r="12" fill="#000"/>
      </g>
      <g fill="#00a8ec">
        <circle cx="600" cy="287" r="4.5"/>
        <circle cx="539" cy="345" r="4.5"/><circle cx="660" cy="345" r="4.5"/>
        <circle cx="539" cy="426" r="4.5"/><circle cx="660" cy="426" r="4.5"/>
      </g>
    </svg>
    <div class="center eyebrow" style="top:86px">Services</div>
    <h2 class="center" style="top:109px">Empowering Companies,<br>Elevating Careers.</h2>
    <p class="center" style="top:206px;left:280px;width:640px">Lorem Ipsum is simply dummy text of the printing and typesetting industry. Lorem Ipsum has been the industry's standard dummy text ever since the 1500s.</p>
    <div class="svc-label" style="right:681px;top:333px;text-align:right">Work from Office<br>Full-Timers</div>
    <div class="svc-label" style="left:681px;top:333px">Work from Home<br>Full-Timers</div>
    <div class="svc-label" style="right:681px;top:414px;text-align:right">Work from Office<br>Contractors</div>
    <div class="svc-label" style="left:681px;top:414px">Work from Home<br>Contractors</div>
    <div class="btn light" style="left:512px;top:496px;width:176px;height:34px">Learn More</div>
  </section>

  <section class="careers">
    <div class="brand">TRTS</div>
    <div class="divider"></div>
    <div class="eyebrow">Careers Job Search</div>
    <h2>We Find the Right Fit<br>for Every Role</h2>
    <div class="btn light" style="left:549px;top:172px;width:176px;height:33px">Search</div>
  </section>

  <section class="contact">
    <div class="center eyebrow" style="top:2231px">Contact Us</div>
    <h2 class="center" style="top:2252px">Get in Touch With Us</h2>
    <p class="center" style="top:2310px;left:310px;width:580px">Lorem Ipsum is simply dummy text of the printing and typesetting industry. Lorem Ipsum has been the industry's standard dummy text ever since the 1500s,</p>
    <div class="field" style="top:2384px">Name</div>
    <div class="field" style="top:2430px">Email</div>
    <div class="field" style="top:2477px">Number</div>
    <div class="field area" style="top:2524px">Message</div>
    <div class="btn" style="left:534px;top:2701px;width:134px;height:34px">Send</div>
  </section>

  <footer class="footer">
    <div class="brand">TRTS</div>
    <p class="about-text">Lorem Ipsum is simply dummy text of the printing and typesetting industry. Lorem Ipsum has been the industry's standard dummy text ever since the 1500s,</p>
    <div class="social" style="left:188px;background:#1877f2"></div>
    <div class="social" style="left:228px;background:#d6307a"></div>
    <div class="social" style="left:268px;background:#0a8fd8"></div>
    <h4 style="left:518px">Quick Links</h4>
    <ul>
      <li>Home</li>
      <li>About Us</li>
      <li>Services</li>
      <li>Careers Job Search</li>
      <li>Employers Contact Us</li>
      <li>Candidates Register your interest</li>
    </ul>
    <h4 style="left:772px">Subscribe Our Newsletter</h4>
    <div class="newsletter-field">Email Address</div>
    <div class="btn" style="left:772px;top:177px;width:134px;height:34px">Subscribe</div>
  </footer>

  <div class="copyright">Copyright@2024-All Rights Reserved</div>
</div>
</body>
</html>
```